Plakat-Design für Verkauf von Bio-zertifiziertem Saatgut
Zielgruppe
Wir sind ein Start Up und verkaufen BIO Zertifiziertes Saatgut für Gemüse, Kräuter, Heilpflanzen und essbare Sprossen etc. Zielgruppe ist vor allem die DIY Community von Jung bis Alt.
Aufgabenstellung
*** INFO*** Da es keine 'Kalender'-Projekte gibt, sollten wir das Projekt unter 'Plakat' einstellen ***INFO***
Wir sind auf der Suche nach einem Design für einen Monatskalender (Deckblatt, 12 Monate, Schlussblatt) der als ewiger Aussaatkalender fungieren soll (Keine Jahreszahlen, nur der Monat). Jeden Monat sollen die Sorten gezeigt werden die jetzt ausgesät werden können. Am Besten teilweise (nicht alle) als Illustrationen oder Bilder. Die Sorten orientieren sich an unserem Saatgutsortiment. Als Unterteilung kann man: 'Vorzucht im Haus', Frühbeet' und 'Direktsaat'
Die Informationen welche Samen wann ausgesät werden, kommen von uns. (Erstmal Platzhalter für das Design nutzen) Falls der Designer Erfahrung in diesem Bereich hat, kann er die Informationen auch selber einfügen. Sonst ist der Designer für Layout und Illustrationen/Bilder zuständig. Toll wäre wenn für jeden Monat noch eine 'Bauernweisheit' zum Thema Pflanzen / Aussaat / Garten hinzugefügt werden kann.
Das Design soll sich an unserer CI der Website www.keimfeld.de orientieren. Logo, Farben und Fonts (My-Everything, BW Mitga) sind im Anhang beigefügt. Auch die Vorlage der Druckerei ist beigefügt. Format: DIN A4 hoch (210 x 297 mm), beidseitig bedruckt so das man den Kalender auch Aufgeklappt nutzen kann.
Falls noch Informationen benötigt werden, dann meldet euch gerne!

```html
<!DOCTYPE html>
<html lang="de">
<head>
<meta charset="utf-8">
<title>Aussaatkalender – Monatsblätter</title>
<link href="https://fonts.googleapis.com/css2?family=Allura&family=Montserrat:wght@400;600;700&display=swap" rel="stylesheet">
<style>
  :root{
    --paper:#ffffff;
    --sand:#eee8dc;
    --sand-dark:#e3dbcc;
    --leaf-1:#8fae7c;
    --leaf-2:#4f7a4a;
    --zucchini-1:#7ea36a;
    --zucchini-2:#3f6a3c;
    --radish:#c2283a;
    --seed-1:#c9a77e;
    --seed-2:#8a6a48;
  }
  *{box-sizing:border-box;margin:0;padding:0}
  html,body{width:1200px;height:1200px;overflow:hidden;background:var(--paper)}
  body{font-family:"Montserrat",Arial,sans-serif;position:relative}

  .calendar-grid{
    position:absolute;left:71px;top:48px;
    display:grid;grid-template-columns:repeat(4,261px);grid-template-rows:repeat(3,368px);
    column-gap:17px;row-gap:22px;
  }
  .page{position:relative;width:261px;height:368px;overflow:hidden;background:var(--light)}
  .m-jan{--dark:#c9d4d6;--light:#e4eaea;--accent:#94a8ab;--ink:#2f4f56;--title:#2f4f56}
  .m-feb{--dark:#c3dbd8;--light:#e0ecea;--accent:#a0c6c2;--ink:#2d5552;--title:#2d5552}
  .m-mar{--dark:#d8ddc8;--light:#eceee2;--accent:#b6c09b;--ink:#4d5a2c;--title:#7e8d4a}
  .m-apr{--dark:#e8ecd0;--light:#f4f5e8;--accent:#d2dd9c;--ink:#6d7d22;--title:#a8bb3a}
  .m-may{--dark:#ded4df;--light:#efe9ef;--accent:#bdabc1;--ink:#5b3d64;--title:#7a4f86}
  .m-jun{--dark:#e9d7e9;--light:#f5ebf5;--accent:#d9b7d9;--ink:#7a4584;--title:#9a5aa4}
  .m-jul{--dark:#f7e0ca;--light:#fbefe4;--accent:#f5c8a0;--ink:#c86f22;--title:#e8903a}
  .m-aug{--dark:#fadcd5;--light:#fdece8;--accent:#f6b9af;--ink:#c8604f;--title:#e8877a}
  .m-sep{--dark:#fde8bd;--light:#fef5de;--accent:#fcd487;--ink:#d28d10;--title:#f0a820}
  .m-oct{--dark:#eed3cd;--light:#f6e7e3;--accent:#dba79d;--ink:#8e3a2c;--title:#b2503e}
  .m-nov{--dark:#e3d3d7;--light:#f0e7e9;--accent:#c4a3aa;--ink:#5e2a35;--title:#7a3a45}
  .m-dec{--dark:#d7cdc1;--light:#ebe6de;--accent:#b19e88;--ink:#4a3826;--title:#5e4a36}

  .panel-left{position:absolute;left:0;top:0;width:130px;height:100%;background:var(--dark)}

  .spinach-art{
    position:absolute;left:134px;top:-6px;width:132px;height:100px;
    border-radius:48% 30% 55% 45%;
    background:radial-gradient(ellipse at 45% 45%,var(--leaf-1),var(--leaf-2) 75%,transparent 76%);
  }

  .section-title{
    position:absolute;font-weight:700;font-size:7.5px;letter-spacing:.3px;color:var(--ink);
    text-align:center;width:80px;
  }
  .direkt-title{left:24px;top:60px}
  .frueh-title{left:157px;top:128px}

  .arch-icon{position:absolute;left:44px;top:71px;width:40px;height:22px}

  .seed-list{position:absolute;list-style:none;display:flex;flex-direction:column;gap:1px}
  .seed-list li{
    height:9px;line-height:9px;font-size:5px;padding-left:3px;color:var(--ink);
    background:color-mix(in srgb,var(--accent) 70%,transparent);
  }
  .direkt-a{left:19px;top:94px;width:46px}
  .direkt-b{left:67px;top:94px;width:46px}

  .frueh-box{
    position:absolute;left:174px;top:137px;width:47px;height:155px;
    background:color-mix(in srgb,var(--accent) 55%,transparent);
    border-radius:24px 24px 0 0;
  }
  .frueh-box svg{position:absolute;left:13px;top:7px}
  .frueh-list{left:174px;top:163px;width:47px}
  .frueh-list li{background:color-mix(in srgb,var(--accent) 65%,transparent)}

  .vegetable-art{
    position:absolute;left:52px;top:222px;width:106px;height:70px;
    border-radius:60% 40% 50% 50% / 60% 50% 50% 40%;
    transform:rotate(-14deg);
    background:linear-gradient(100deg,var(--zucchini-1),var(--zucchini-2) 70%,var(--radish) 90%);
  }

  .ground-band{
    position:absolute;left:0;bottom:0;width:100%;height:72px;background:var(--sand);
    clip-path:polygon(0 9px,6% 4px,12% 10px,19% 3px,27% 8px,35% 2px,44% 9px,52% 4px,61% 10px,70% 3px,78% 8px,86% 2px,93% 9px,100% 5px,100% 100%,0 100%);
  }
  .seed-art{
    position:absolute;left:112px;top:326px;width:92px;height:42px;border-radius:40% 40% 0 0;
    background:radial-gradient(ellipse at 60% 80%,var(--seed-2),var(--seed-1) 55%,transparent 75%);
  }
  .month-name{
    position:absolute;left:20px;top:306px;font-family:"Allura",cursive;font-size:30px;
    line-height:1;color:var(--title);white-space:nowrap;
  }
  .month-sub{
    position:absolute;left:45px;top:347px;font-weight:700;font-size:9px;color:var(--ink);
  }
  .brand-mark{
    position:absolute;left:218px;top:336px;display:flex;align-items:center;gap:2px;
    font-size:4px;font-weight:600;color:var(--leaf-2);
  }
  .brand-mark .dot{width:13px;height:13px;border-radius:50%;border:1.5px solid var(--leaf-2)}
</style>
</head>
<body>
<main class="calendar-grid">

<!-- Each month sheet -->
<article class="page m-jan">
  <div class="panel-left"></div>
  <div class="spinach-art" role="img" aria-label="Illustration von Spinatblättern"></div>
  <h2 class="section-title direkt-title">DIREKTSAAT</h2>
  <svg class="arch-icon" viewBox="0 0 40 22"><path d="M0 22 A20 20 0 0 1 40 22 Z" fill="var(--accent)"/><path d="M12 12 h10 l4 -3 M13 15 h12" stroke="var(--ink)" stroke-width="1" fill="none"/></svg>
  <ul class="seed-list direkt-a"><li>Radieschen</li><li>Aubergine</li><li>Gurke</li><li>Kopfsalat</li><li>Blumenkohl</li><li>Brokkoli</li><li>Bohnen</li><li>Aubergine</li><li>Blumenkohl</li><li>Gurke</li><li>Brokkoli</li><li>Radieschen</li><li>Blumenkohl</li><li>Brokkoli</li><li>Kopfsalat</li></ul>
  <ul class="seed-list direkt-b"><li>Radieschen</li><li>Aubergine</li><li>Gurke</li><li>Kopfsalat</li><li>Blumenkohl</li><li>Brokkoli</li><li>Bohnen</li><li>Aubergine</li><li>Blumenkohl</li><li>Gurke</li><li>Brokkoli</li><li>Radieschen</li></ul>
  <h2 class="section-title frueh-title">FRÜHBEET</h2>
  <div class="frueh-box"><svg width="21" height="16" viewBox="0 0 21 16"><path d="M2 6 L10.5 2 L19 6 V14 H2 Z M2 6 H19 M10.5 2 V14" stroke="var(--ink)" stroke-width="1.2" fill="none"/></svg></div>
  <ul class="seed-list frueh-list"><li>Radieschen</li><li>Aubergine</li><li>Gurke</li><li>Kopfsalat</li><li>Blumenkohl</li><li>Brokkoli</li><li>Bohnen</li><li>Radieschen</li><li>Gurke</li><li>Spitzkohl</li><li>Aubergine</li><li>Bohnen</li><li>Radieschen</li></ul>
  <div class="vegetable-art" role="img" aria-label="Illustration einer Zucchini mit Radieschen"></div>
  <div class="ground-band"></div>
  <div class="seed-art" role="img" aria-label="Illustration verstreuter Samenkörner"></div>
  <p class="month-name">Januar</p><p class="month-sub">Aussaat</p>
  <div class="brand-mark"><span class="dot"></span></div>
</article>

<article class="page m-feb">
  <div class="panel-left"></div>
  <div class="spinach-art" role="img" aria-label="Illustration von Spinatblättern"></div>
  <h2 class="section-title direkt-title">DIREKTSAAT</h2>
  <svg class="arch-icon" viewBox="0 0 40 22"><path d="M0 22 A20 20 0 0 1 40 22 Z" fill="var(--accent)"/><path d="M12 12 h10 l4 -3 M13 15 h12" stroke="var(--ink)" stroke-width="1" fill="none"/></svg>
  <ul class="seed-list direkt-a"><li>Radieschen</li><li>Aubergine</li><li>Gurke</li><li>Kopfsalat</li><li>Blumenkohl</li><li>Brokkoli</li><li>Bohnen</li><li>Aubergine</li><li>Blumenkohl</li><li>Gurke</li><li>Brokkoli</li><li>Radieschen</li><li>Blumenkohl</li><li>Brokkoli</li><li>Kopfsalat</li></ul>
  <ul class="seed-list direkt-b"><li>Radieschen</li><li>Aubergine</li><li>Gurke</li><li>Kopfsalat</li><li>Blumenkohl</li><li>Brokkoli</li><li>Bohnen</li><li>Aubergine</li><li>Blumenkohl</li><li>Gurke</li><li>Brokkoli</li><li>Radieschen</li></ul>
  <h2 class="section-title frueh-title">FRÜHBEET</h2>
  <div class="frueh-box"><svg width="21" height="16" viewBox="0 0 21 16"><path d="M2 6 L10.5 2 L19 6 V14 H2 Z M2 6 H19 M10.5 2 V14" stroke="var(--ink)" stroke-width="1.2" fill="none"/></svg></div>
  <ul class="seed-list frueh-list"><li>Radieschen</li><li>Aubergine</li><li>Gurke</li><li>Kopfsalat</li><li>Blumenkohl</li><li>Brokkoli</li><li>Bohnen</li><li>Radieschen</li><li>Gurke</li><li>Spitzkohl</li><li>Aubergine</li><li>Bohnen</li><li>Radieschen</li></ul>
  <div class="vegetable-art" role="img" aria-label="Illustration einer Zucchini mit Radieschen"></div>
  <div class="ground-band"></div>
  <div class="seed-art" role="img" aria-label="Illustration verstreuter Samenkörner"></div>
  <p class="month-name">Februar</p><p class="month-sub">Aussaat</p>
  <div class="brand-mark"><span class="dot"></span></div>
</article>

<article class="page m-mar">
  <div class="panel-left"></div>
  <div class="spinach-art" role="img" aria-label="Illustration von Spinatblättern"></div>
  <h2 class="section-title direkt-title">DIREKTSAAT</h2>
  <svg class="arch-icon" viewBox="0 0 40 22"><path d="M0 22 A20 20 0 0 1 40 22 Z" fill="var(--accent)"/><path d="M12 12 h10 l4 -3 M13 15 h12" stroke="var(--ink)" stroke-width="1" fill="none"/></svg>
  <ul class="seed-list direkt-a"><li>Radieschen</li><li>Aubergine</li><li>Gurke</li><li>Kopfsalat</li><li>Blumenkohl</li><li>Brokkoli</li><li>Bohnen</li><li>Aubergine</li><li>Blumenkohl</li><li>Gurke</li><li>Brokkoli</li><li>Radieschen</li><li>Blumenkohl</li><li>Brokkoli</li><li>Kopfsalat</li></ul>
  <ul class="seed-list direkt-b"><li>Radieschen</li><li>Aubergine</li><li>Gurke</li><li>Kopfsalat</li><li>Blumenkohl</li><li>Brokkoli</li><li>Bohnen</li><li>Aubergine</li><li>Blumenkohl</li><li>Gurke</li><li>Brokkoli</li><li>Radieschen</li></ul>
  <h2 class="section-title frueh-title">FRÜHBEET</h2>
  <div class="frueh-box"><svg width="21" height="16" viewBox="0 0 21 16"><path d="M2 6 L10.5 2 L19 6 V14 H2 Z M2 6 H19 M10.5 2 V14" stroke="var(--ink)" stroke-width="1.2" fill="none"/></svg></div>
  <ul class="seed-list frueh-list"><li>Radieschen</li><li>Aubergine</li><li>Gurke</li><li>Kopfsalat</li><li>Blumenkohl</li><li>Brokkoli</li><li>Bohnen</li><li>Radieschen</li><li>Gurke</li><li>Spitzkohl</li><li>Aubergine</li><li>Bohnen</li><li>Radieschen</li></ul>
  <div class="vegetable-art" role="img" aria-label="Illustration einer Zucchini mit Radieschen"></div>
  <div class="ground-band"></div>
  <div class="seed-art" role="img" aria-label="Illustration verstreuter Samenkörner"></div>
  <p class="month-name">März</p><p class="month-sub" style="left:20px">Aussaat</p>
  <div class="brand-mark"><span class="dot"></span></div>
</article>

<article class="page m-apr">
  <div class="panel-left"></div>
  <div class="spinach-art" role="img" aria-label="Illustration von Spinatblättern"></div>
  <h2 class="section-title direkt-title">DIREKTSAAT</h2>
  <svg class="arch-icon" viewBox="0 0 40 22"><path d="M0 22 A20 20 0 0 1 40 22 Z" fill="var(--accent)"/><path d="M12 12 h10 l4 -3 M13 15 h12" stroke="var(--ink)" stroke-width="1" fill="none"/></svg>
  <ul class="seed-list direkt-a"><li>Radieschen</li><li>Aubergine</li><li>Gurke</li><li>Kopfsalat</li><li>Blumenkohl</li><li>Brokkoli</li><li>Bohnen</li><li>Aubergine</li><li>Blumenkohl</li><li>Gurke</li><li>Brokkoli</li><li>Radieschen</li><li>Blumenkohl</li><li>Brokkoli</li><li>Kopfsalat</li></ul>
  <ul class="seed-list direkt-b"><li>Radieschen</li><li>Aubergine</li><li>Gurke</li><li>Kopfsalat</li><li>Blumenkohl</li><li>Brokkoli</li><li>Bohnen</li><li>Aubergine</li><li>Blumenkohl</li><li>Gurke</li><li>Brokkoli</li><li>Radieschen</li></ul>
  <h2 class="section-title frueh-title">FRÜHBEET</h2>
  <div class="frueh-box"><svg width="21" height="16" viewBox="0 0 21 16"><path d="M2 6 L10.5 2 L19 6 V14 H2 Z M2 6 H19 M10.5 2 V14" stroke="var(--ink)" stroke-width="1.2" fill="none"/></svg></div>
  <ul class="seed-list frueh-list"><li>Radieschen</li><li>Aubergine</li><li>Gurke</li><li>Kopfsalat</li><li>Blumenkohl</li><li>Brokkoli</li><li>Bohnen</li><li>Radieschen</li><li>Gurke</li><li>Spitzkohl</li><li>Aubergine</li><li>Bohnen</li><li>Radieschen</li></ul>
  <div class="vegetable-art" role="img" aria-label="Illustration einer Zucchini mit Radieschen"></div>
  <div class="ground-band"></div>
  <div class="seed-art" role="img" aria-label="Illustration verstreuter Samenkörner"></div>
  <p class="month-name">April</p><p class="month-sub">Aussaat</p>
  <div class="brand-mark"><span class="dot"></span></div>
</article>

<article class="page m-may">
  <div class="panel-left"></div>
  <div class="spinach-art" role="img" aria-label="Illustration von Spinatblättern"></div>
  <h2 class="section-title direkt-title">DIREKTSAAT</h2>
  <svg class="arch-icon" viewBox="0 0 40 22"><path d="M0 22 A20 20 0 0 1 40 22 Z" fill="var(--accent)"/><path d="M12 12 h10 l4 -3 M13 15 h12" stroke="var(--ink)" stroke-width="1" fill="none"/></svg>
  <ul class="seed-list direkt-a"><li>Radieschen</li><li>Aubergine</li><li>Gurke</li><li>Kopfsalat</li><li>Blumenkohl</li><li>Brokkoli</li><li>Bohnen</li><li>Aubergine</li><li>Blumenkohl</li><li>Gurke</li><li>Brokkoli</li><li>Radieschen</li><li>Blumenkohl</li><li>Brokkoli</li><li>Kopfsalat</li></ul>
  <ul class="seed-list direkt-b"><li>Radieschen</li><li>Aubergine</li><li>Gurke</li><li>Kopfsalat</li><li>Blumenkohl</li><li>Brokkoli</li><li>Bohnen</li><li>Aubergine</li><li>Blumenkohl</li><li>Gurke</li><li>Brokkoli</li><li>Radieschen</li></ul>
  <h2 class="section-title frueh-title">FRÜHBEET</h2>
  <div class="frueh-box"><svg width="21" height="16" viewBox="0 0 21 16"><path d="M2 6 L10.5 2 L19 6 V14 H2 Z M2 6 H19 M10.5 2 V14" stroke="var(--ink)" stroke-width="1.2" fill="none"/></svg></div>
  <ul class="seed-list frueh-list"><li>Radieschen</li><li>Aubergine</li><li>Gurke</li><li>Kopfsalat</li><li>Blumenkohl</li><li>Brokkoli</li><li>Bohnen</li><li>Radieschen</li><li>Gurke</li><li>Spitzkohl</li><li>Aubergine</li><li>Bohnen</li><li>Radieschen</li></ul>
  <div class="vegetable-art" role="img" aria-label="Illustration einer Zucchini mit Radieschen"></div>
  <div class="ground-band"></div>
  <div class="seed-art" role="img" aria-label="Illustration verstreuter Samenkörner"></div>
  <p class="month-name">Mai</p><p class="month-sub">Aussaat</p>
  <div class="brand-mark"><span class="dot"></span></div>
</article>

<article class="page m-jun">
  <div class="panel-left"></div>
  <div class="spinach-art" role="img" aria-label="Illustration von Spinatblättern"></div>
  <h2 class="section-title direkt-title">DIREKTSAAT</h2>
  <svg class="arch-icon" viewBox="0 0 40 22"><path d="M0 22 A20 20 0 0 1 40 22 Z" fill="var(--accent)"/><path d="M12 12 h10 l4 -3 M13 15 h12" stroke="var(--ink)" stroke-width="1" fill="none"/></svg>
  <ul class="seed-list direkt-a"><li>Radieschen</li><li>Aubergine</li><li>Gurke</li><li>Kopfsalat</li><li>Blumenkohl</li><li>Brokkoli</li><li>Bohnen</li><li>Aubergine</li><li>Blumenkohl</li><li>Gurke</li><li>Brokkoli</li><li>Radieschen</li><li>Blumenkohl</li><li>Brokkoli</li><li>Kopfsalat</li></ul>
  <ul class="seed-list direkt-b"><li>Radieschen</li><li>Aubergine</li><li>Gurke</li><li>Kopfsalat</li><li>Blumenkohl</li><li>Brokkoli</li><li>Bohnen</li><li>Aubergine</li><li>Blumenkohl</li><li>Gurke</li><li>Brokkoli</li><li>Radieschen</li></ul>
  <h2 class="section-title frueh-title">FRÜHBEET</h2>
  <div class="frueh-box"><svg width="21" height="16" viewBox="0 0 21 16"><path d="M2 6 L10.5 2 L19 6 V14 H2 Z M2 6 H19 M10.5 2 V14" stroke="var(--ink)" stroke-width="1.2" fill="none"/></svg></div>
  <ul class="seed-list frueh-list"><li>Radieschen</li><li>Aubergine</li><li>Gurke</li><li>Kopfsalat</li><li>Blumenkohl</li><li>Brokkoli</li><li>Bohnen</li><li>Radieschen</li><li>Gurke</li><li>Spitzkohl</li><li>Aubergine</li><li>Bohnen</li><li>Radieschen</li></ul>
  <div class="vegetable-art" role="img" aria-label="Illustration einer Zucchini mit Radieschen"></div>
  <div class="ground-band"></div>
  <div class="seed-art" role="img" aria-label="Illustration verstreuter Samenkörner"></div>
  <p class="month-name">Juni</p><p class="month-sub">Aussaat</p>
  <div class="brand-mark"><span class="dot"></span></div>
</article>

<article class="page m-jul">
  <div class="panel-left"></div>
  <div class="spinach-art" role="img" aria-label="Illustration von Spinatblättern"></div>
  <h2 class="section-title direkt-title">DIREKTSAAT</h2>
  <svg class="arch-icon" viewBox="0 0 40 22"><path d="M0 22 A20 20 0 0 1 40 22 Z" fill="var(--accent)"/><path d="M12 12 h10 l4 -3 M13 15 h12" stroke="var(--ink)" stroke-width="1" fill="none"/></svg>
  <ul class="seed-list direkt-a"><li>Radieschen</li><li>Aubergine</li><li>Gurke</li><li>Kopfsalat</li><li>Blumenkohl</li><li>Brokkoli</li><li>Bohnen</li><li>Aubergine</li><li>Blumenkohl</li><li>Gurke</li><li>Brokkoli</li><li>Radieschen</li><li>Blumenkohl</li><li>Brokkoli</li><li>Kopfsalat</li></ul>
  <ul class="seed-list direkt-b"><li>Radieschen</li><li>Aubergine</li><li>Gurke</li><li>Kopfsalat</li><li>Blumenkohl</li><li>Brokkoli</li><li>Bohnen</li><li>Aubergine</li><li>Blumenkohl</li><li>Gurke</li><li>Brokkoli</li><li>Radieschen</li></ul>
  <h2 class="section-title frueh-title">FRÜHBEET</h2>
  <div class="frueh-box"><svg width="21" height="16" viewBox="0 0 21 16"><path d="M2 6 L10.5 2 L19 6 V14 H2 Z M2 6 H19 M10.5 2 V14" stroke="var(--ink)" stroke-width="1.2" fill="none"/></svg></div>
  <ul class="seed-list frueh-list"><li>Radieschen</li><li>Aubergine</li><li>Gurke</li><li>Kopfsalat</li><li>Blumenkohl</li><li>Brokkoli</li><li>Bohnen</li><li>Radieschen</li><li>Gurke</li><li>Spitzkohl</li><li>Aubergine</li><li>Bohnen</li><li>Radieschen</li></ul>
  <div class="vegetable-art" role="img" aria-label="Illustration einer Zucchini mit Radieschen"></div>
  <div class="ground-band"></div>
  <div class="seed-art" role="img" aria-label="Illustration verstreuter Samenkörner"></div>
  <p class="month-name">Juli</p><p class="month-sub">Aussaat</p>
  <div class="brand-mark"><span class="dot"></span></div>
</article>

<article class="page m-aug">
  <div class="panel-left"></div>
  <div class="spinach-art" role="img" aria-label="Illustration von Spinatblättern"></div>
  <h2 class="section-title direkt-title">DIREKTSAAT</h2>
  <svg class="arch-icon" viewBox="0 0 40 22"><path d="M0 22 A20 20 0 0 1 40 22 Z" fill="var(--accent)"/><path d="M12 12 h10 l4 -3 M13 15 h12" stroke="var(--ink)" stroke-width="1" fill="none"/></svg>
  <ul class="seed-list direkt-a"><li>Radieschen</li><li>Aubergine</li><li>Gurke</li><li>Kopfsalat</li><li>Blumenkohl</li><li>Brokkoli</li><li>Bohnen</li><li>Aubergine</li><li>Blumenkohl</li><li>Gurke</li><li>Brokkoli</li><li>Radieschen</li><li>Blumenkohl</li><li>Brokkoli</li><li>Kopfsalat</li></ul>
  <ul class="seed-list direkt-b"><li>Radieschen</li><li>Aubergine</li><li>Gurke</li><li>Kopfsalat</li><li>Blumenkohl</li><li>Brokkoli</li><li>Bohnen</li><li>Aubergine</li><li>Blumenkohl</li><li>Gurke</li><li>Brokkoli</li><li>Radieschen</li></ul>
  <h2 class="section-title frueh-title">FRÜHBEET</h2>
  <div class="frueh-box"><svg width="21" height="16" viewBox="0 0 21 16"><path d="M2 6 L10.5 2 L19 6 V14 H2 Z M2 6 H19 M10.5 2 V14" stroke="var(--ink)" stroke-width="1.2" fill="none"/></svg></div>
  <ul class="seed-list frueh-list"><li>Radieschen</li><li>Aubergine</li><li>Gurke</li><li>Kopfsalat</li><li>Blumenkohl</li><li>Brokkoli</li><li>Bohnen</li><li>Radieschen</li><li>Gurke</li><li>Spitzkohl</li><li>Aubergine</li><li>Bohnen</li><li>Radieschen</li></ul>
  <div class="vegetable-art" role="img" aria-label="Illustration einer Zucchini mit Radieschen"></div>
  <div class="ground-band"></div>
  <div class="seed-art" role="img" aria-label="Illustration verstreuter Samenkörner"></div>
  <p class="month-name">August</p><p class="month-sub" style="left:62px">Aussaat</p>
  <div class="brand-mark"><span class="dot"></span></div>
</article>

<article class="page m-sep">
  <div class="panel-left"></div>
  <div class="spinach-art" role="img" aria-label="Illustration von Spinatblättern"></div>
  <h2 class="section-title direkt-title">DIREKTSAAT</h2>
  <svg class="arch-icon" viewBox="0 0 40 22"><path d="M0 22 A20 20 0 0 1 40 22 Z" fill="var(--accent)"/><path d="M12 12 h10 l4 -3 M13 15 h12" stroke="var(--ink)" stroke-width="1" fill="none"/></svg>
  <ul class="seed-list direkt-a"><li>Radieschen</li><li>Aubergine</li><li>Gurke</li><li>Kopfsalat</li><li>Blumenkohl</li><li>Brokkoli</li><li>Bohnen</li><li>Aubergine</li><li>Blumenkohl</li><li>Gurke</li><li>Brokkoli</li><li>Radieschen</li><li>Blumenkohl</li><li>Brokkoli</li><li>Kopfsalat</li></ul>
  <ul class="seed-list direkt-b"><li>Radieschen</li><li>Aubergine</li><li>Gurke</li><li>Kopfsalat</li><li>Blumenkohl</li><li>Brokkoli</li><li>Bohnen</li><li>Aubergine</li><li>Blumenkohl</li><li>Gurke</li><li>Brokkoli</li><li>Radieschen</li></ul>
  <h2 class="section-title frueh-title">FRÜHBEET</h2>
  <div class="frueh-box"><svg width="21" height="16" viewBox="0 0 21 16"><path d="M2 6 L10.5 2 L19 6 V14 H2 Z M2 6 H19 M10.5 2 V14" stroke="var(--ink)" stroke-width="1.2" fill="none"/></svg></div>
  <ul class="seed-list frueh-list"><li>Radieschen</li><li>Aubergine</li><li>Gurke</li><li>Kopfsalat</li><li>Blumenkohl</li><li>Brokkoli</li><li>Bohnen</li><li>Radieschen</li><li>Gurke</li><li>Spitzkohl</li><li>Aubergine</li><li>Bohnen</li><li>Radieschen</li></ul>
  <div class="vegetable-art" role="img" aria-label="Illustration einer Zucchini mit Radieschen"></div>
  <div class="ground-band"></div>
  <div class="seed-art" role="img" aria-label="Illustration verstreuter Samenkörner"></div>
  <p class="month-name">September</p><p class="month-sub">Aussaat</p>
  <div class="brand-mark"><span class="dot"></span></div>
</article>

<article class="page m-oct">
  <div class="panel-left"></div>
  <div class="spinach-art" role="img" aria-label="Illustration von Spinatblättern"></div>
  <h2 class="section-title direkt-title">DIREKTSAAT</h2>
  <svg class="arch-icon" viewBox="0 0 40 22"><path d="M0 22 A20 20 0 0 1 40 22 Z" fill="var(--accent)"/><path d="M12 12 h10 l4 -3 M13 15 h12" stroke="var(--ink)" stroke-width="1" fill="none"/></svg>
  <ul class="seed-list direkt-a"><li>Radieschen</li><li>Aubergine</li><li>Gurke</li><li>Kopfsalat</li><li>Blumenkohl</li><li>Brokkoli</li><li>Bohnen</li><li>Aubergine</li><li>Blumenkohl</li><li>Gurke</li><li>Brokkoli</li><li>Radieschen</li><li>Blumenkohl</li><li>Brokkoli</li><li>Kopfsalat</li></ul>
  <ul class="seed-list direkt-b"><li>Radieschen</li><li>Aubergine</li><li>Gurke</li><li>Kopfsalat</li><li>Blumenkohl</li><li>Brokkoli</li><li>Bohnen</li><li>Aubergine</li><li>Blumenkohl</li><li>Gurke</li><li>Brokkoli</li><li>Radieschen</li></ul>
  <h2 class="section-title frueh-title">FRÜHBEET</h2>
  <div class="frueh-box"><svg width="21" height="16" viewBox="0 0 21 16"><path d="M2 6 L10.5 2 L19 6 V14 H2 Z M2 6 H19 M10.5 2 V14" stroke="var(--ink)" stroke-width="1.2" fill="none"/></svg></div>
  <ul class="seed-list frueh-list"><li>Radieschen</li><li>Aubergine</li><li>Gurke</li><li>Kopfsalat</li><li>Blumenkohl</li><li>Brokkoli</li><li>Bohnen</li><li>Radieschen</li><li>Gurke</li><li>Spitzkohl</li><li>Aubergine</li><li>Bohnen</li><li>Radieschen</li></ul>
  <div class="vegetable-art" role="img" aria-label="Illustration einer Zucchini mit Radieschen"></div>
  <div class="ground-band"></div>
  <div class="seed-art" role="img" aria-label="Illustration verstreuter Samenkörner"></div>
  <p class="month-name">Oktober</p><p class="month-sub">Aussaat</p>
  <div class="brand-mark"><span class="dot"></span></div>
</article>

<article class="page m-nov">
  <div class="panel-left"></div>
  <div class="spinach-art" role="img" aria-label="Illustration von Spinatblättern"></div>
  <h2 class="section-title direkt-title">DIREKTSAAT</h2>
  <svg class="arch-icon" viewBox="0 0 40 22"><path d="M0 22 A20 20 0 0 1 40 22 Z" fill="var(--accent)"/><path d="M12 12 h10 l4 -3 M13 15 h12" stroke="var(--ink)" stroke-width="1" fill="none"/></svg>
  <ul class="seed-list direkt-a"><li>Radieschen</li><li>Aubergine</li><li>Gurke</li><li>Kopfsalat</li><li>Blumenkohl</li><li>Brokkoli</li><li>Bohnen</li><li>Aubergine</li><li>Blumenkohl</li><li>Gurke</li><li>Brokkoli</li><li>Radieschen</li><li>Blumenkohl</li><li>Brokkoli</li><li>Kopfsalat</li></ul>
  <ul class="seed-list direkt-b"><li>Radieschen</li><li>Aubergine</li><li>Gurke</li><li>Kopfsalat</li><li>Blumenkohl</li><li>Brokkoli</li><li>Bohnen</li><li>Aubergine</li><li>Blumenkohl</li><li>Gurke</li><li>Brokkoli</li><li>Radieschen</li></ul>
  <h2 class="section-title frueh-title">FRÜHBEET</h2>
  <div class="frueh-box"><svg width="21" height="16" viewBox="0 0 21 16"><path d="M2 6 L10.5 2 L19 6 V14 H2 Z M2 6 H19 M10.5 2 V14" stroke="var(--ink)" stroke-width="1.2" fill="none"/></svg></div>
  <ul class="seed-list frueh-list"><li>Radieschen</li><li>Aubergine</li><li>Gurke</li><li>Kopfsalat</li><li>Blumenkohl</li><li>Brokkoli</li><li>Bohnen</li><li>Radieschen</li><li>Gurke</li><li>Spitzkohl</li><li>Aubergine</li><li>Bohnen</li><li>Radieschen</li></ul>
  <div class="vegetable-art" role="img" aria-label="Illustration einer Zucchini mit Radieschen"></div>
  <div class="ground-band"></div>
  <div class="seed-art" role="img" aria-label="Illustration verstreuter Samenkörner"></div>
  <p class="month-name">November</p><p class="month-sub">Aussaat</p>
  <div class="brand-mark"><span class="dot"></span></div>
</article>

<article class="page m-dec">
  <div class="panel-left"></div>
  <div class="spinach-art" role="img" aria-label="Illustration von Spinatblättern"></div>
  <h2 class="section-title direkt-title">DIREKTSAAT</h2>
  <svg class="arch-icon" viewBox="0 0 40 22"><path d="M0 22 A20 20 0 0 1 40 22 Z" fill="var(--accent)"/><path d="M12 12 h10 l4 -3 M13 15 h12" stroke="var(--ink)" stroke-width="1" fill="none"/></svg>
  <ul class="seed-list direkt-a"><li>Radieschen</li><li>Aubergine</li><li>Gurke</li><li>Kopfsalat</li><li>Blumenkohl</li><li>Brokkoli</li><li>Bohnen</li><li>Aubergine</li><li>Blumenkohl</li><li>Gurke</li><li>Brokkoli</li><li>Radieschen</li><li>Blumenkohl</li><li>Brokkoli</li><li>Kopfsalat</li></ul>
  <ul class="seed-list direkt-b"><li>Radieschen</li><li>Aubergine</li><li>Gurke</li><li>Kopfsalat</li><li>Blumenkohl</li><li>Brokkoli</li><li>Bohnen</li><li>Aubergine</li><li>Blumenkohl</li><li>Gurke</li><li>Brokkoli</li><li>Radieschen</li></ul>
  <h2 class="section-title frueh-title">FRÜHBEET</h2>
  <div class="frueh-box"><svg width="21" height="16" viewBox="0 0 21 16"><path d="M2 6 L10.5 2 L19 6 V14 H2 Z M2 6 H19 M10.5 2 V14" stroke="var(--ink)" stroke-width="1.2" fill="none"/></svg></div>
  <ul class="seed-list frueh-list"><li>Radieschen</li><li>Aubergine</li><li>Gurke</li><li>Kopfsalat</li><li>Blumenkohl</li><li>Brokkoli</li><li>Bohnen</li><li>Radieschen</li><li>Gurke</li><li>Spitzkohl</li><li>Aubergine</li><li>Bohnen</li><li>Radieschen</li></ul>
  <div class="vegetable-art" role="img" aria-label="Illustration einer Zucchini mit Radieschen"></div>
  <div class="ground-band"></div>
  <div class="seed-art" role="img" aria-label="Illustration verstreuter Samenkörner"></div>
  <p class="month-name">Dezember</p><p class="month-sub" style="left:55px">Aussaat</p>
  <div class="brand-mark"><span class="dot"></span></div>
</article>

</main>
</body>
</html>
```